New business blog needs wordpress theme

I need a unique wordpress theme for my new business oriented blog at quietharlow.net. The blog focuses on my experience as an entrepreneur and offers insights into business problems while chronicling my experience building a new company.

I would like to see a theme that looks more like a creative professional's website, not a business website. Large photos, bright colors, unique layout. I do not want stock photos of people in suits doing business type things. Also, no pictures of me - I am blogging anonymously.

The design should communicate technology and beauty - for example, I really like the feel of the landing page at www.pebblyn.net - it is beautiful to look at but also reflects the cutting edge nature of what they are doing.

Industry/Entity Type

Business

```html
<!DOCTYPE html>
<html lang="en">
<head>
<meta charset="utf-8">
<title>Quiet Harlow</title>
<link rel="stylesheet" href="https://fonts.googleapis.com/css2?family=Dosis:wght@400;500;600;700&family=Open+Sans:wght@400;600&display=swap">
<style>
:root{
  --orange:#ee9a62;
  --orange-deep:#e3874c;
  --ink:#2b2b2b;
  --hero-ink:#3a2a20;
  --text:#444;
  --muted:#8a8a8a;
  --rule:#e2e2e2;
  --panel:#eeeeee;
  --link:#e0692e;
  --white:#fff;
}
*{margin:0;padding:0;box-sizing:border-box}
html,body{width:1200px;height:2281px;overflow:hidden;background:var(--white)}
body{position:relative;font-family:"Open Sans",Arial,sans-serif;color:var(--text)}
.hero{position:absolute;left:0;top:0;width:1200px;height:707px;
  background:radial-gradient(ellipse at 30% 40%,#f9c39c 0%,transparent 55%),
             radial-gradient(ellipse at 80% 20%,#f4ab7c 0%,transparent 50%),
             linear-gradient(180deg,#f3a875 0%,#ee9662 100%)}
.topbar{position:absolute;left:0;top:0;width:1200px;height:108px;border-bottom:1px solid rgba(255,255,255,.35)}
.brand{position:absolute;left:137px;top:14px;color:var(--white)}
.brand-name{font-family:"Dosis",sans-serif;font-weight:500;font-size:36px;line-height:40px}
.brand-tag{font-size:12.5px;line-height:17px;width:340px;margin-top:4px}
.nav{position:absolute;right:140px;top:60px;display:flex;gap:30px;color:var(--white);font-size:13px;font-weight:600}
.feature-art{position:absolute;left:148px;top:467px;width:390px;height:185px;border-radius:4px;
  background:linear-gradient(135deg,#f5f1ea 0%,#cfe2ea 45%,#e9d26a 70%,#d9685c 100%)}
.feature{position:absolute;left:418px;top:278px;width:642px;text-align:right}
.feature h1{font-family:"Dosis",sans-serif;font-weight:500;font-size:38px;line-height:48px;letter-spacing:1px;color:var(--hero-ink)}
.feature .meta{margin-top:10px;font-size:11px;color:#5a3a28;justify-content:flex-end}
.feature p{width:450px;margin-left:auto;font-size:13px;line-height:19px;color:var(--hero-ink);margin-top:16px}
.feature .more{margin-top:12px;color:var(--white);font-size:13px}
.meta{display:flex;gap:22px;align-items:center;font-size:11px;color:var(--muted)}
.meta span{display:flex;align-items:center;gap:6px}
.meta svg{width:12px;height:12px;fill:currentColor}
.post{position:absolute;left:137px;width:643px;border-bottom:1px solid var(--rule)}
.post h2{font-family:"Dosis",sans-serif;font-weight:700;font-size:27px;line-height:33px;text-transform:uppercase;color:var(--ink)}
.post .meta{margin-top:12px;height:24px}
.share{margin-left:auto;display:flex;gap:5px}
.share b{font-weight:400;border:1px solid #d4d4d4;border-radius:3px;padding:3px 8px;font-size:11px;color:#666}
.post-body{display:flex;gap:30px;margin-top:12px}
.thumb{flex:0 0 183px;height:190px}
.thumb.book{background:linear-gradient(180deg,#f3cf3e 0%,#f0c43a 55%,#6fb14a 100%)}
.thumb.road{background:linear-gradient(180deg,#9ec3e4 0%,#cfe0ee 45%,#a39a78 62%,#7c7560 100%)}
.excerpt{font-size:12.3px;line-height:20.5px;color:var(--text)}
.excerpt em{font-style:normal;color:var(--link)}
.pager{position:absolute;left:137px;top:2160px;display:flex;gap:16px;align-items:center;font-size:13px;color:var(--orange-deep)}
.pager .current{background:#e3e3e3;color:#555;padding:2px 7px}
.pager .count{margin-left:18px}
.sidebar{position:absolute;left:826px;top:760px;width:232px}
.search{display:flex;height:36px}
.search div{flex:1;border:1px solid #ddd;font-size:11px;color:#aaa;padding:10px 8px}
.search span{width:36px;background:var(--orange);display:flex;align-items:center;justify-content:center}
.widget{background:var(--panel);margin-top:26px}
.widget h3{background:var(--orange);color:var(--white);font-family:"Dosis",sans-serif;font-weight:600;font-size:19px;padding:8px 12px}
.recent li{list-style:none;display:flex;gap:12px;padding:14px 10px;border-bottom:1px solid #e0e0e0;font-size:11.5px;line-height:15px;color:#444;height:89px}
.recent i{flex:0 0 44px;height:42px;display:block}
.recent i.book{background:linear-gradient(180deg,#f3cf3e,#6fb14a)}
.recent i.cards{background:linear-gradient(135deg,#f5f1ea,#e9d26a,#d9685c)}
.recent em{font-style:normal;color:var(--link)}
.top li{list-style:none;font-size:12px;color:#666;padding:8px 12px;border-bottom:1px solid #e0e0e0;text-transform:uppercase}
.top li::before{content:"› ";color:#999}
.footer{position:absolute;left:0;top:2224px;width:1200px;border-top:1px solid var(--rule);height:57px;font-size:11.5px;color:#777}
.footer .copy{position:absolute;left:137px;top:18px}
.footer .links{position:absolute;right:140px;top:18px;display:flex;gap:10px}
</style>
</head>
<body>
<header class="hero">
  <div class="topbar">
    <div class="brand">
      <div class="brand-name">Quiet Harlow</div>
      <div class="brand-tag">Harlow talks business. Best practices, articles and tips and about small business in the United States</div>
    </div>
    <nav class="nav"><span>Home</span><span>Small Business</span><span>Technology</span><span>About Harlow</span><span>Contact</span></nav>
  </div>
  <div class="feature-art" role="img" aria-label="Postcards and a stack of direct mail flyers"></div>
  <div class="feature">
    <h1>Comparing Direct Mail to Dealcrowd<br>– By the Numbers</h1>
    <div class="meta"><span><svg viewBox="0 0 12 12"><circle cx="6" cy="4" r="3"/><path d="M0 12a6 5 0 0 1 12 0z"/></svg>by Harlow</span><span><svg viewBox="0 0 12 12"><path d="M1 2h10v10H1zM2 5v6h8V5z"/></svg>06 Mar 2014</span><span><svg viewBox="0 0 12 12"><ellipse cx="6" cy="5" rx="6" ry="4"/></svg>No Comments</span></div>
    <p>Unhappy with the results of a direct mail (snail mail) campaign, I decided to compare the results to a Dealcrowd campaign. I compared both the cost of the respective campaigns, the revenue generated, the customers acquired and customer retention.</p>
    <p>One of my businesses owns and operates franchised hair salons. We have 15 salons across 2 different brands. The company builds new salons and buys and rehabilitates old salons. One brand is a value focused family salon, the other is a high-end male oriented barbershop.</p>
    <div class="more">[ Read More ]</div>
  </div>
</header>

<article class="post" style="top:752px;height:342px">
  <h2>Finally dumping Chatterloop on Orbis – any recommendations for an SMS app?</h2>
  <div class="meta"><span><svg viewBox="0 0 12 12"><circle cx="6" cy="4" r="3"/><path d="M0 12a6 5 0 0 1 12 0z"/></svg>by Harlow</span><span><svg viewBox="0 0 12 12"><path d="M1 2h10v10H1zM2 5v6h8V5z"/></svg>06 Mar 2014</span><span><svg viewBox="0 0 12 12"><ellipse cx="6" cy="5" rx="6" ry="4"/></svg>No Comments</span>
    <div class="share"><b>Chirpline</b><b>Friendwall</b><b>Gridwell</b><b>Like</b></div></div>
  <div class="post-body">
    <div class="thumb book" role="img" aria-label="Book cover with a crocodile illustration"></div>
    <p class="excerpt">I am embarrassed how long I tried to make Chatterloop on Orbis work. Chatterloop is Gridwell's default SMS client for Orbis Toffee. It combines SMS with Gridwell's chat/video product called Chatterloop. Online, Chatterloop is excellent. It allows you to chat or video with your email contacts, collaboratively work on web documents, have group video chats, etc. On the phone it is painfully slow. Trying to view or send out a text message can take forever.<br>All my business run on Gridwell – email, documents, spreadsheets, chat, video – I am drinking the Fizzmix and I love it. It is <em>[...]</em></p>
  </div>
</article>

<article class="post" style="top:1124px;height:318px">
  <h2>The Who &amp; The Why</h2>
  <div class="meta"><span><svg viewBox="0 0 12 12"><circle cx="6" cy="4" r="3"/><path d="M0 12a6 5 0 0 1 12 0z"/></svg>by Harlow</span><span><svg viewBox="0 0 12 12"><path d="M1 2h10v10H1zM2 5v6h8V5z"/></svg>06 Mar 2014</span><span><svg viewBox="0 0 12 12"><ellipse cx="6" cy="5" rx="6" ry="4"/></svg>No Comments</span></div>
  <div class="post-body">
    <div class="thumb road" role="img" aria-label="Roadside highway sign in a desert landscape"></div>
    <p class="excerpt">I am embarrassed how long I tried to make Chatterloop on Orbis work. Chatterloop is Gridwell's default SMS client for Orbis Toffee. It combines SMS with Gridwell's chat/video product called Chatterloop. Online, Chatterloop is excellent. It allows you to chat or video with your email contacts, collaboratively work on web documents, have group video chats, etc. On the phone it is painfully slow. Trying to view or send out a text message can take forever.<br>All my business run on Gridwell – email, documents, spreadsheets, chat, video – I am drinking the Fizzmix and I love it. It is <em>[...]</em></p>
  </div>
</article>

<article class="post" style="top:1468px;height:318px">
  <h2>The Who &amp; The Why</h2>
  <div class="meta"><span><svg viewBox="0 0 12 12"><circle cx="6" cy="4" r="3"/><path d="M0 12a6 5 0 0 1 12 0z"/></svg>by Harlow</span><span><svg viewBox="0 0 12 12"><path d="M1 2h10v10H1zM2 5v6h8V5z"/></svg>06 Mar 2014</span><span><svg viewBox="0 0 12 12"><ellipse cx="6" cy="5" rx="6" ry="4"/></svg>No Comments</span></div>
  <div class="post-body">
    <div class="thumb road" role="img" aria-label="Roadside highway sign in a desert landscape"></div>
    <p class="excerpt">I am embarrassed how long I tried to make Chatterloop on Orbis work. Chatterloop is Gridwell's default SMS client for Orbis Toffee. It combines SMS with Gridwell's chat/video product called Chatterloop. Online, Chatterloop is excellent. It allows you to chat or video with your email contacts, collaboratively work on web documents, have group video chats, etc. On the phone it is painfully slow. Trying to view or send out a text message can take forever.<br>All my business run on Gridwell – email, documents, spreadsheets, chat, video – I am drinking the Fizzmix and I love it. It is <em>[...]</em></p>
  </div>
</article>

<article class="post" style="top:1812px;height:330px">
  <h2>The Who &amp; The Why</h2>
  <div class="meta"><span><svg viewBox="0 0 12 12"><circle cx="6" cy="4" r="3"/><path d="M0 12a6 5 0 0 1 12 0z"/></svg>by Harlow</span><span><svg viewBox="0 0 12 12"><path d="M1 2h10v10H1zM2 5v6h8V5z"/></svg>06 Mar 2014</span><span><svg viewBox="0 0 12 12"><ellipse cx="6" cy="5" rx="6" ry="4"/></svg>No Comments</span></div>
  <div class="post-body">
    <div class="thumb road" role="img" aria-label="Roadside highway sign in a desert landscape"></div>
    <p class="excerpt">I am embarrassed how long I tried to make Chatterloop on Orbis work. Chatterloop is Gridwell's default SMS client for Orbis Toffee. It combines SMS with Gridwell's chat/video product called Chatterloop. Online, Chatterloop is excellent. It allows you to chat or video with your email contacts, collaboratively work on web documents, have group video chats, etc. On the phone it is painfully slow. Trying to view or send out a text message can take forever.<br>All my business run on Gridwell – email, documents, spreadsheets, chat, video – I am drinking the Fizzmix and I love it. It is <em>[...]</em></p>
  </div>
</article>

<nav class="pager"><span class="current">1</span><span>2</span><span>3</span><span>4</span><span>5</span><span>6</span><span>»</span><span>10</span><span>20</span><span>30</span><span>Last »</span><span>...</span><span class="count">Page 1 of 50</span></nav>

<aside class="sidebar">
  <div class="search"><div>Search here...</div><span><svg width="16" height="16" viewBox="0 0 16 16" fill="none" stroke="#fff" stroke-width="2.2"><circle cx="6.5" cy="6.5" r="4.5"/><path d="M10 10l4.5 4.5"/></svg></span></div>
  <section class="widget">
    <h3>Recent Post</h3>
    <ul class="recent">
      <li><i class="cards" role="img" aria-label="Direct mail postcards"></i><span>Comparing Direct Mail to Dealcrowd – By the Numbers <em>[...]</em></span></li>
      <li><i class="book" role="img" aria-label="Book cover"></i><span>Finally Dumping Chatterloop on Orbis – Any <em>[...]</em></span></li>
      <li><i class="book" role="img" aria-label="Book cover"></i><span>The Who &amp; The Why<br><br><em>[...]</em></span></li>
      <li><i class="book" role="img" aria-label="Book cover"></i><span>Comparing Direct Mail to Dealcrowd – By the Numbers <em>[...]</em></span></li>
      <li style="border-bottom:0"><i class="book" role="img" aria-label="Book cover"></i><span>Comparing Direct Mail to Dealcrowd – By the Numbers <em>[...]</em></span></li>
    </ul>
  </section>
  <section class="widget">
    <h3>Top Post</h3>
    <ul class="top">
      <li>quietharlow.net</li><li>theme.pressfolio.net</li><li>quietharlow.net</li><li>theme.pressfolio.net</li>
      <li>quietharlow.net</li><li>theme.pressfolio.net</li><li>quietharlow.net</li><li style="border-bottom:0">theme.pressfolio.net</li>
    </ul>
  </section>
</aside>

<footer class="footer">
  <div class="copy">© 2014 Quiet Harlow | All Right Reserved</div>
  <div class="links"><span>Home</span>|<span>Small Business</span>|<span>Technology</span>|<span>About Harlow</span>|<span>Contact</span></div>
</footer>
</body>
</html>
```